Toddler Music Class Bussiness Needs Web Design

We are a small start up called "WeeBopplings" providing music classes to kids from 6 months to 3 years of age. Kids are instructor led and learn to play a variety of instruments (e.g. drums, tambourines, ukulele's, castanets, etc..), develop coordination and rhythm, and stimulate mental development while having a blast of a time along with other kids and their parents.
The website design needs to be clever, have clean lines, simple modern font, original, fun and colourful and professional. It will need to look good when viewed across different devices and be able to scale well when resized.
This website needs to convey the message that the classes will be enjoyed by parents and children, be safe and contribute to the development of their children.
We have a logo that needs to be incorporated into the design and lead the approach. There will be a number of web pages illustrated in the site map accompanied with this project. The winning bid will have a design that represents a number of pages of the website e.g. 4/5 of the pages

****** commercial in confidence ******
Updates

Reason: Hi Designers, appreciate the design submissions thus far. We have decided to extend tge deadline due to requests from designers :)

Just wanted to say thanks for the designs sent through, there are a few good ones (:

In general we are looking for a little more of a playful approach and have included a few variations on the logos to encourage different design approaches.

Feel free to have a play!!

Target Market(s)

Parents in Australia (multicultural) aged 25 to 45

Industry/Entity Type

Learn

Requirements
Must have
• The website design needs to be clever, have clean lines, simple modern font, original, fun and colourful and professional. It will need to look good when viewed across different devices and be able to scale well when resized.
We have a logo that needs to be incorporated into the design and lead the approach.

```html
<!DOCTYPE html>
<html lang="en">
<head>
<meta charset="utf-8">
<title>WeeBopplings – The Academy For Musical Tots</title>
<link href="https://fonts.googleapis.com/css2?family=Delius&family=Fredoka:wght@500;600&display=swap" rel="stylesheet">
<style>
:root{
  --red:#e3001b;
  --purple:#9b2f8f;
  --orange:#f39200;
  --green:#1a9e3a;
  --cyan:#1aafe0;
  --blue:#0a6fb5;
  --text:#555;
  --line:#e2e2e2;
  --page:#fbfbfb;
  --footer:#f0f0f0;
}
*{box-sizing:border-box;margin:0;padding:0}
html,body{width:925px;height:1200px;overflow:hidden}
body{position:relative;background:var(--page);font-family:"Delius",cursive;color:var(--text)}
.abs{position:absolute}

.brand{left:122px;top:30px}
.brand-name{font-family:"Fredoka",sans-serif;font-weight:600;font-size:34px;color:var(--purple);display:flex;align-items:center;gap:10px}
.brand-name .dot{width:22px;height:22px;background:var(--orange);border-radius:50%}
.brand-tag{font-size:13px;color:#222;margin-top:4px;margin-left:32px}

.search{left:682px;top:18px;width:120px;height:21px;border:1px solid #ddd;border-radius:11px;background:#fff;font-size:8px;color:#aaa;padding:5px 0 0 6px}
.search svg{position:absolute;right:7px;top:5px}

.nav{left:121px;top:122px;width:82px}
.nav a{display:flex;flex-direction:column;align-items:center;justify-content:flex-end;height:52px;margin-bottom:2px;color:#fff;text-decoration:none;font-family:"Fredoka",sans-serif;font-weight:500;font-size:11.5px;padding-bottom:6px;border-radius:3px 0 0 3px}
.nav svg{margin-bottom:4px}
.n1{background:var(--red)}.n2{background:var(--purple)}.n3{background:var(--orange)}.n4{background:var(--green)}.n5{background:var(--cyan)}

.hero{left:203px;top:95px;width:601px;height:333px;border-radius:8px 26px 26px 8px;background:linear-gradient(120deg,#e9f2e4 0%,#cfe6c2 35%,#f4ede9 60%,#dbeccd 100%);box-shadow:0 2px 5px rgba(0,0,0,.15)}
.hero-caption{left:482px;top:209px;width:280px;height:79px;background:rgba(195,60,170,.85);color:#fff;font-family:"Fredoka",sans-serif;font-weight:500;font-size:19px;line-height:25px;padding:11px 15px}
.hero-cta{left:661px;top:289px;width:101px;height:31px;background:var(--cyan);color:#fff;font-family:"Fredoka",sans-serif;font-weight:500;font-size:14px;text-align:center;line-height:31px}
.dots{left:735px;top:387px;display:flex;gap:5px}
.dots span{width:13px;height:13px;border-radius:50%;background:#fff}
.dots span:first-child{background:var(--orange)}

h2{position:absolute;font-weight:400;font-size:18px}
.h-welcome{left:122px;top:447px;color:var(--red)}
.h-classes{left:527px;top:447px;color:var(--purple)}
.h-test{left:121px;top:863px;color:var(--purple)}
.h-gallery{left:525px;top:863px;color:var(--green)}

.welcome-img{left:128px;top:481px;width:383px;height:191px;border-radius:10px;background:linear-gradient(90deg,#8cb25a,#c7dca7 50%,#9cc8e6)}
.copy{font-size:10.5px;line-height:20px;color:#666}
.welcome-copy{left:127px;top:684px;width:388px}

.classes{left:527px;top:481px;width:269px;height:339px;background:#fff;border-radius:8px;box-shadow:0 1px 5px rgba(0,0,0,.15)}
.classes table{border-collapse:collapse;width:100%;font-size:11px}
.classes th{font-weight:400;font-size:17px;color:#444;text-align:left;height:47px;padding:6px 10px 0 10px}
.classes td{height:39px;padding:0 10px;border-top:1px solid var(--line);letter-spacing:-.2px}
.classes td+td,.classes th+th{border-left:1px solid var(--line);font-size:12.5px}
.classes th+th{font-size:17px}
.c-or{color:var(--orange)}.c-gr{color:var(--green)}.c-cy{color:var(--cyan)}.c-rd{color:var(--red)}.c-bl{color:var(--blue)}.c-pu{color:var(--purple)}

.avatar{left:133px;top:922px;width:99px;height:99px;border-radius:50%;background:radial-gradient(circle,#d9a27a 0 40%,var(--orange) 42%)}
.person{left:128px;top:1026px;width:110px;text-align:center}
.person b{display:block;font-weight:400;font-size:12px;color:#777}
.person i{display:block;font-style:normal;font-size:10px;color:var(--purple)}
.quote{left:232px;top:915px;font-family:"Fredoka",sans-serif;font-weight:600;font-size:46px;color:var(--purple);line-height:1}
.test-copy{left:259px;top:943px;width:255px}

.gallery{left:527px;top:907px;width:269px;height:158px;background:#fff;border-radius:12px;box-shadow:0 1px 5px rgba(0,0,0,.15);padding:0 6px}
.gallery-img{width:257px;height:151px;border-radius:10px;background:linear-gradient(120deg,#f4f4f4 30%,#e7d8c6 60%,#c9413a 100%)}
.gallery svg{position:absolute;top:66px}

.footer{left:0;top:1120px;width:925px;height:80px;background:var(--footer)}
.footer-links{left:122px;top:1140px;font-size:10.5px;color:#444;word-spacing:2px}
.footer-copy{left:122px;top:1165px;font-size:10.5px;color:#444}
.social{left:740px;top:1152px;font-size:11px;color:#444;display:flex;gap:12px}
</style>
</head>
<body>

<div class="abs brand">
  <div class="brand-name"><span class="dot"></span>WeeBopplings</div>
  <div class="brand-tag">The Academy For Musical Tots</div>
</div>

<div class="abs search">Search
  <svg width="8" height="8" viewBox="0 0 8 8"><circle cx="3" cy="3" r="2.3" fill="none" stroke="#aaa"/><path d="M5 5l2.5 2.5" stroke="#aaa"/></svg>
</div>

<nav class="abs nav">
  <a class="n1" href="#"><svg width="20" height="18" viewBox="0 0 20 18"><ellipse cx="10" cy="6" rx="7" ry="3" fill="none" stroke="#fff" stroke-width="2"/><path d="M3 6v7c0 2 14 2 14 0V6" fill="none" stroke="#fff" stroke-width="2"/></svg>About Us</a>
  <a class="n2" href="#"><svg width="22" height="20" viewBox="0 0 22 20"><circle cx="11" cy="10" r="7.5" fill="none" stroke="#fff" stroke-width="2.5"/></svg>Classes</a>
  <a class="n3" href="#"><svg width="24" height="18" viewBox="0 0 24 18"><circle cx="7" cy="12" r="5" fill="#fff"/><path d="M10 9L22 2" stroke="#fff" stroke-width="2.5"/></svg>Enrol</a>
  <a class="n4" href="#"><svg width="24" height="18" viewBox="0 0 24 18"><path d="M12 17C4 11 6 2 12 6c6-4 8 5 0 11z" fill="#fff"/></svg>Contact Us</a>
  <a class="n5" href="#"><svg width="22" height="16" viewBox="0 0 22 16"><path d="M4 3h12v6a6 6 0 0 1-12 0z" fill="#fff"/><path d="M2 15h18" stroke="#fff" stroke-width="2"/></svg>Merchandise</a>
</nav>

<div class="abs hero" role="img" aria-label="Photo of a smiling toddler in a pink dress playing a tambourine in a bright room"></div>
<div class="abs hero-caption">Music classes to kids from 6 months to 3 years of age</div>
<div class="abs hero-cta">Get Started</div>
<div class="abs dots"><span></span><span></span><span></span></div>

<h2 class="h-welcome">Welcome to Wee Bopplings</h2>
<div class="abs welcome-img" role="img" aria-label="Photo of a baby holding a tambourine outdoors"></div>
<p class="abs copy welcome-copy">Lorem Ipsum is simply dummy text of the printing and typesetting industry. Lorem Ipsum has been the industry's standard dummy text ever since the 1500s, when an unknown printer took a galley of type and scrambled it to make a type specimen book. It has survived not only five centuries, but also the leap into electronic typesetting, remaining essentially unchanged. It was popularised in the 1960s with the release of Letraset sheets containing Lorem Ipsum passages, and more recently with desktop publishing software I</p>

<h2 class="h-classes">Classes</h2>
<div class="abs classes">
  <table>
    <tr><th>Class</th><th>Time</th></tr>
    <tr class="c-or"><td>Mon - Drums,Tambourines</td><td>9:30 am -1.00 pm</td></tr>
    <tr class="c-gr"><td>Tue - Ukulele's</td><td>9:30 am -1.00 pm</td></tr>
    <tr class="c-cy"><td>Wed - Casinetts,Tambourines</td><td>9:30 am -1.00 pm</td></tr>
    <tr class="c-rd"><td>Thu - Holiday</td><td>N/A</td></tr>
    <tr class="c-bl"><td>Fri- Casinetts,Tambourines</td><td>9:30 am -1.00 pm</td></tr>
    <tr class="c-pu"><td>Sat- Casinetts,Tambourines</td><td>9:30 am -1.00 pm</td></tr>
    <tr class="c-rd"><td>Sun - Holiday</td><td>N/A</td></tr>
  </table>
</div>

<h2 class="h-test">Parent's Testimonials</h2>
<div class="abs avatar" role="img" aria-label="Portrait of the parent inside an orange flower frame"></div>
<div class="abs person"><b>Daniel Rowe</b><i>Buisness Man</i></div>
<div class="abs quote">“</div>
<p class="abs copy test-copy">Lorem Ipsum is simply dummy text of the printing and typesetting industry. Lorem Ipsum has been the industry's standard dummy text ever since the 1500s, when an unknown printer took a galley of type and scrambled it to make a type specimen book.</p>

<h2 class="h-gallery">Photo Gallery</h2>
<div class="abs gallery">
  <div class="gallery-img" role="img" aria-label="Photo of a toddler playing a red drum kit"></div>
  <svg style="left:14px" width="14" height="22" viewBox="0 0 14 22"><path d="M11 2L3 11l8 9" fill="none" stroke="#fff" stroke-width="3"/></svg>
  <svg style="right:14px" width="14" height="22" viewBox="0 0 14 22"><path d="M3 2l8 9-8 9" fill="none" stroke="#fff" stroke-width="3"/></svg>
</div>

<footer class="abs footer"></footer>
<div class="abs footer-links">About Us &nbsp;| Classes &nbsp;| &nbsp;Enrol &nbsp;| &nbsp;Contact Us &nbsp;| &nbsp;Merchandise</div>
<div class="abs footer-copy">© 2014 Company Name ,All Rights Reserved</div>
<div class="abs social"><span>Chirper</span><span>Friendbook</span></div>

</body>
</html>
```